Business card and coffee mug

Hello, I need a business card design and a coffee mug. Here is the info for the business card front and back. It is for an architecture company.

For the front

-Add my phone number

214-883-2761

For the back

-New Construction

-Exterior additions

-Interior Finish outs

-MEP’s

```html
<!DOCTYPE html>
<html lang="en">
<head>
<meta charset="utf-8">
<title>Ridgeline Design Studio LLC – Business Cards</title>
<link href="https://fonts.googleapis.com/css2?family=Montserrat:wght@500;700&display=swap" rel="stylesheet">
<style>
  :root {
    --bg: #e6e6e8;
    --card: #ffffff;
    --teal: #2a7489;
    --teal-dark: #1f5f71;
    --navy: #253746;
    --red: #e0525a;
    --shadow: rgba(0,0,0,0.12);
  }
  * { margin: 0; padding: 0; box-sizing: border-box; }
  html, body {
    width: 1200px; height: 900px; overflow: hidden;
    background: var(--bg);
    font-family: "Montserrat", Arial, sans-serif;
  }
  .stage {
    width: 1200px; height: 900px;
    display: flex; align-items: center; justify-content: center; gap: 60px;
  }
  .card {
    width: 500px; height: 300px;
    background: var(--card);
    border-radius: 26px;
    box-shadow: 0 10px 30px var(--shadow);
    position: relative;
    display: flex; flex-direction: column; align-items: center; justify-content: center;
  }
  .brand {
    display: flex; align-items: center; gap: 10px;
    color: var(--navy);
    font-weight: 700;
    font-size: 22px;
    letter-spacing: 0.5px;
    text-transform: uppercase;
  }
  .brand-mark {
    width: 22px; height: 22px;
    background: var(--red);
    flex: none;
  }
  .brand-rule {
    width: 250px; height: 2px; background: var(--teal);
    margin-top: 8px;
  }
  .services {
    list-style: none;
    display: grid;
    grid-template-columns: 1fr 1fr;
    column-gap: 70px; row-gap: 10px;
    margin-top: 28px;
    color: var(--teal);
    font-weight: 500;
    font-size: 14px;
  }
  .services li { display: flex; align-items: center; gap: 8px; }
  .services svg { width: 12px; height: 12px; flex: none; }
  .phone-band {
    margin-top: 14px;
    width: 360px; height: 30px;
    background: linear-gradient(90deg, var(--teal-dark), var(--teal) 50%, var(--teal-dark));
    display: flex; align-items: center; justify-content: center; gap: 12px;
    color: #fff;
    font-weight: 500;
    font-size: 16px;
    letter-spacing: 4px;
  }
  .phone-band svg { width: 14px; height: 14px; }
</style>
</head>
<body>
<main class="stage">
  <section class="card card-back">
    <div class="brand"><span class="brand-mark"></span>Ridgeline Design Studio LLC</div>
    <div class="brand-rule"></div>
    <ul class="services">
      <li><svg viewBox="0 0 12 12"><rect x="1" y="1" width="10" height="10" fill="none" stroke="#e0525a" stroke-width="1.5"/><path d="M3 6l2 2 4-4" fill="none" stroke="#e0525a" stroke-width="1.5"/></svg>New Construction</li>
      <li><svg viewBox="0 0 12 12"><rect x="1" y="1" width="10" height="10" fill="none" stroke="#e0525a" stroke-width="1.5"/><path d="M3 6l2 2 4-4" fill="none" stroke="#e0525a" stroke-width="1.5"/></svg>Exterior additions</li>
      <li><svg viewBox="0 0 12 12"><rect x="1" y="1" width="10" height="10" fill="none" stroke="#e0525a" stroke-width="1.5"/><path d="M3 6l2 2 4-4" fill="none" stroke="#e0525a" stroke-width="1.5"/></svg>Interior Finish outs</li>
      <li><svg viewBox="0 0 12 12"><rect x="1" y="1" width="10" height="10" fill="none" stroke="#e0525a" stroke-width="1.5"/><path d="M3 6l2 2 4-4" fill="none" stroke="#e0525a" stroke-width="1.5"/></svg>MEP’s</li>
    </ul>
  </section>

  <section class="card card-front">
    <div class="brand"><span class="brand-mark"></span>Ridgeline Design Studio LLC</div>
    <div class="phone-band">
      <svg viewBox="0 0 24 24"><path fill="#fff" d="M6.6 10.8a15.1 15.1 0 0 0 6.6 6.6l2.2-2.2a1 1 0 0 1 1-.25 11.4 11.4 0 0 0 3.6.57 1 1 0 0 1 1 1V20a1 1 0 0 1-1 1A17 17 0 0 1 3 4a1 1 0 0 1 1-1h3.5a1 1 0 0 1 1 1c0 1.25.2 2.45.57 3.57a1 1 0 0 1-.25 1z"/></svg>
      <span class="phone-number">214-883-2761</span>
    </div>
  </section>
</main>
</body>
</html>
```